Business Card Design Project

Hi Designers, this project is currently on hold until the Logo is completed:
Please submit to the Logo project here:
http://work.pitchvault.example/brief.aspx?id=413907

Once logo is completed, it will be attached to this project for you to create business cards with show logo, company name and address

Maren T R Quillby

Osric's Tiny Grey Heron Co.
Fernbrook
Nether Coombsby
North Devon EX91 4TZ

Tel: 01809 417356
Mobile: 07900 263818
email: maren@tiny-grey-heron.example.co.uk

Project Deadline Extended
Reason: Sorry everyone, we have had a sick ewe and I am now behind with this one and need to extend the deadline. Best wishes Maren

The designer who wins the logo brief will be asked to design the business card. Many thanks Maren

Project Deadline Extended
Reason: Sorry everyone, just a chaotic time of year with animals. Need to extend the deadline again..... as I just haven't had enough time to take a good look.... Thank you for your understanding. Maren

Project Deadline Extended
Reason: Sorry everyone It is our busiest time of year with animals and just no time to spend going through such great designs. I will have to extend the deadline again and hopefully have some news very soon. Wishing you all a very happy Christmas and a happy and healthy new year. Maren & Osric

High end market
Boutique restaurants for meat (it's not commercial lamb it's a slow matured quality meat more like venison/beef) expensive - specialized market

High End shoot clothing / wool / sheepskin rugs
Quality products

Business

• based on the logo - (which Pitch Vault has just been asked to do)
possibly based on a simplified picture of a Hebridean Ram (shows it's a Hebridean by it's horns as opposed to other black sheep!!)

```html
<!DOCTYPE html>
<html lang="en">
<head>
<meta charset="utf-8">
<title>Osric's Tiny Grey Heron Co. — Business Card</title>
<link rel="stylesheet" href="https://fonts.googleapis.com/css2?family=Cinzel:wght@400;700&display=swap">
<style>
  :root {
    --ink: #2a2a2a;
    --card: #f4f2ed;
    --backdrop: #d8d5cf;
    --reverse: #f4f2ed;
  }
  * { box-sizing: border-box; margin: 0; padding: 0; }
  html, body {
    width: 1200px;
    height: 800px;
    overflow: hidden;
    background: var(--backdrop);
  }
  .business-card {
    position: absolute;
    left: 75px;
    top: 100px;
    width: 1050px;
    height: 600px;
    background: var(--card);
    overflow: hidden;
    font-family: "Cinzel", Georgia, serif;
    color: var(--ink);
    box-shadow: 0 6px 24px rgba(0,0,0,0.18);
  }
  .corner-band {
    position: absolute;
    inset: 0;
    width: 1050px;
    height: 600px;
  }
  .brand {
    position: absolute;
    left: 60px;
    top: 95px;
    width: 200px;
    text-align: center;
  }
  .brand-dot {
    width: 118px;
    height: 118px;
    margin: 0 auto 18px;
    border: 9px solid var(--ink);
    border-radius: 50%;
  }
  .brand-name {
    font-size: 38px;
    font-weight: 400;
    letter-spacing: 3px;
    line-height: 1;
  }
  .brand-tagline {
    font-size: 10px;
    font-weight: 400;
    letter-spacing: 2.5px;
    margin-top: 6px;
  }
  .holder {
    position: absolute;
    left: 120px;
    top: 395px;
  }
  .holder-rule {
    width: 140px;
    height: 3px;
    background: var(--ink);
    margin-bottom: 14px;
  }
  .holder-name {
    font-size: 30px;
    font-weight: 700;
    letter-spacing: 0.5px;
    text-transform: uppercase;
    line-height: 1;
  }
  .address {
    font-style: normal;
    font-size: 12px;
    line-height: 20px;
    margin-top: 14px;
    text-transform: uppercase;
  }
  .contact {
    position: absolute;
    left: 500px;
    top: 405px;
    list-style: none;
    font-size: 11px;
    line-height: 28px;
    text-transform: uppercase;
  }
</style>
</head>
<body>
  <article class="business-card">
    <svg class="corner-band" viewBox="0 0 1050 600" aria-hidden="true">
      <polygon points="330,0 1050,0 1050,420" fill="var(--ink)"/>
      <circle cx="840" cy="175" r="150" fill="none" stroke="var(--reverse)" stroke-width="16"/>
    </svg>

    <header class="brand">
      <div class="brand-dot"></div>
      <p class="brand-name">OSRIC'S</p>
      <p class="brand-tagline">TINY GREY HERON CO.</p>
    </header>

    <section class="holder">
      <div class="holder-rule"></div>
      <h1 class="holder-name">Maren T R Quillby</h1>
      <address class="address">
        Osric's Tiny Grey Heron Co.<br>
        Fernbrook<br>
        Nether Coombsby<br>
        North Devon EX91 4TZ
      </address>
    </section>

    <ul class="contact">
      <li>Tel: 01809 417356</li>
      <li>Mobile: 07900 263818</li>
      <li>Email: maren@tiny-grey-heron.example.co.uk</li>
    </ul>
  </article>
</body>
</html>
```